IT support company needs Banner Ad for the top of their quote layout template

We need a banner Ad for the top of our for quote layout template so it is sent out on all our quotes

The banner size must be 827 x 100 pixels - anything larger than 60 KB can cause upload time issues

We have attached our logo and examples of the quote page to see how it looks in the context of the whole page.

Essential elements of the banner
- Must have our logo but this can be changed to be different colours if it makes the design work better i.e. Tidal Grove could be all in white

Colours
- Can use all of our standard colours - Orange, Black, Grey and White

Images
- As a premium IT support company we deal with people and technology so would like to see both of these Incorporated into the banner i.e. people using technology These images could be watermarked or one colour effect.

Look and Feel
- Professional, friendly, people, technology, premium

Target Market
Small business owners and managers

Industry/Entity Type

It Company

```html
<!DOCTYPE html>
<html lang="nl">
<head>
<meta charset="utf-8">
<title>Offerte MR-000280 – Standard MSP #2</title>
<link rel="stylesheet" href="https://fonts.googleapis.com/css2?family=Carlito:wght@400;700&family=Montserrat:wght@700&display=swap">
<style>
  :root {
    --orange: #f26a21;
    --blue: #2f80c8;
    --rule-blue: #1e73be;
    --head-light: #dcefff;
    --head-mid: #a9d6f5;
    --row-alt: #f2f2f2;
    --ink: #1a1a1a;
    --border: #333;
    --footer: #5dbbea;
    --paper: #ffffff;
  }
  * { box-sizing: border-box; margin: 0; padding: 0; }
  html, body { width: 895px; height: 1200px; overflow: hidden; background: var(--paper); }
  body { font-family: "Carlito", "Calibri", sans-serif; color: var(--ink); font-size: 12.5px; }
  .page {
    position: relative; width: 827px; height: 1109px;
    transform: scale(1.0822); transform-origin: 0 0;
  }
  .abs { position: absolute; }

  /* Banner */
  .banner { left: 0; top: 0; width: 827px; height: 100px; overflow: hidden; }
  .banner-photo {
    position: absolute; left: 270px; top: 0; width: 557px; height: 100px;
    background: linear-gradient(90deg, #6b5a4d 0%, #9c8f86 30%, #c9c6c2 60%, #e4e3e1 100%);
  }
  .banner-orange { position: absolute; inset: 0; }
  .brand {
    position: absolute; left: 40px; top: 35px;
    font-family: "Montserrat", sans-serif; font-weight: 700; font-size: 24px;
    color: #fff; letter-spacing: 0.5px;
  }

  .doc-title { left: 27px; top: 127px; font-size: 21px; }

  .portrait { left: 26px; top: 167px; width: 99px; height: 131px; background: linear-gradient(180deg, #8c8c8c, #4d4d4d); }
  .party { top: 165px; line-height: 17.5px; }
  .party h2 { font-size: 16px; font-weight: 400; color: var(--blue); margin-bottom: 6px; }
  .party b { font-weight: 700; }
  .from { left: 136px; }
  .to { left: 362px; }
  .meta { left: 630px; }

  .rule { left: 26px; top: 310px; width: 777px; height: 3px; background: var(--rule-blue); }

  .section-title { left: 27px; font-size: 18px; }

  table { position: absolute; left: 26px; width: 777px; border-collapse: collapse; border: 1px solid var(--border); }
  th, td { height: 25px; padding: 0 5px; font-size: 12.5px; font-weight: 400; text-align: left; }
  th { background: linear-gradient(90deg, var(--head-mid), var(--head-light) 60%, var(--head-mid)); height: 24px; }
  tbody tr:nth-child(even) td { background: var(--row-alt); }
  .num { text-align: right; border-left: 1px solid var(--border); }
  .col-amt { width: 109px; }
  .col-rec { width: 111px; }

  .totals { right: 29px; text-align: right; line-height: 25px; }
  .totals div { display: flex; justify-content: flex-end; gap: 0; }
  .totals .lbl { color: var(--blue); }
  .totals .val { font-weight: 700; width: 108px; }

  .disclaimer { left: 27px; top: 914px; }
  .sign-line { top: 987px; height: 1px; background: var(--border); }
  .sign-label { top: 990px; }

  .footer { left: 0; top: 1063px; width: 827px; height: 46px;
    background: linear-gradient(90deg, #eaf6fd, #bfe4f7 40%, var(--footer) 60%, #bfe4f7 85%, #eaf6fd); }
  .footer::before { content: ""; position: absolute; left: 0; top: 0; width: 100%; height: 5px; background: #3aa9e0; }
  .footer span { position: absolute; top: 17px; font-size: 12.5px; }
</style>
</head>
<body>
<div class="page">

  <header class="banner abs">
    <div class="banner-photo" role="img" aria-label="Team working together at computers in a bright office"></div>
    <svg class="banner-orange" width="827" height="100" viewBox="0 0 827 100">
      <polygon points="0,0 318,0 283,100 0,100" fill="var(--orange)"/>
      <polygon points="318,0 326,0 291,100 283,100" fill="#fff"/>
    </svg>
    <div class="brand">TIDAL GROVE</div>
  </header>

  <h1 class="doc-title abs" style="font-weight:400">Standard MSP&nbsp; #2</h1>

  <div class="portrait abs" role="img" aria-label="Portrait of the account manager"></div>

  <div class="party from abs">
    <h2>Opgesteld door:</h2>
    <b>Marlow Reyes Ltd</b><br>Marlow Reyes<br><br>Fax<br>marlow.reyes@quotewell.com
  </div>
  <div class="party to abs">
    <h2>Opgesteld voor:</h2>
    <b>Copper Ridge</b><br>2871 Alder Ln.<br>Fairview,&nbsp;&nbsp; 40312<br>Norah Whitfield<br>owen.blake@bluefinch.co.uk
  </div>
  <div class="party meta abs">
    <h2>Gegevens Offerte:</h2>
    <b>Offerte #: MR-000280</b><br>Versie: 1<br>Leverdatum: 14/11/2017<br>Vervaldatum: 31/12/2017
  </div>

  <div class="rule abs"></div>

  <h3 class="section-title abs" style="top:330px;font-weight:400">Overzicht Offerte</h3>
  <table style="top:358px">
    <thead><tr><th>Beschrijving</th><th class="num col-amt">Bedrag</th></tr></thead>
    <tbody><tr><td>Initial Investment</td><td class="num">$800.00</td></tr></tbody>
  </table>
  <div class="totals abs" style="top:413px">
    <div><span class="lbl">Subtotaal:</span><span class="val">$800.00</span></div>
    <div><span class="lbl">VAT:</span><span class="val">$160.00</span></div>
    <div><span class="lbl">Totaal:</span><span class="val">$960.00</span></div>
  </div>

  <h3 class="section-title abs" style="top:507px;font-weight:400">Overzicht Terugkerende Kosten</h3>
  <table style="top:535px">
    <thead><tr><th>Beschrijving</th><th class="num col-amt">Bedrag</th></tr></thead>
    <tbody>
      <tr><td>Monitoring</td><td class="num">$375.00</td></tr>
      <tr><td>Support</td><td class="num">$65.00</td></tr>
      <tr><td>Fixed Hours</td><td class="num">$850.00</td></tr>
    </tbody>
  </table>
  <div class="totals abs" style="top:642px">
    <div><span class="lbl">Terugkerende totaal:</span><span class="val">$1,290.00</span></div>
  </div>

  <h3 class="section-title abs" style="top:685px;font-weight:400">*Optionele kosten</h3>
  <table style="top:713px">
    <thead><tr><th>Beschrijving</th><th class="num col-rec">Recurring</th><th class="num col-amt">One-Time</th></tr></thead>
    <tbody>
      <tr><td>Monitoring</td><td class="num">$790.00</td><td class="num">$0.00</td></tr>
      <tr><td>Support</td><td class="num">$185.00</td><td class="num">$0.00</td></tr>
      <tr><td>Fixed Hours</td><td class="num">$695.00</td><td class="num">$0.00</td></tr>
      <tr><td>Add-on Services</td><td class="num">$850.00</td><td class="num">$0.00</td></tr>
    </tbody>
  </table>
  <div class="totals abs" style="top:847px">
    <div><span class="lbl">Optionele terugkerend bedrag:</span><span class="val">$2,520.00</span></div>
    <div><span class="lbl">Optionele ongeplande Subtotaal:</span><span class="val">$.00</span></div>
  </div>

  <p class="disclaimer abs">Taxes, shipping, handling and other fees may apply.&nbsp; We reserve the right to cancel orders arising from pricing or other errors.</p>

  <div class="sign-line abs" style="left:26px;width:465px"></div>
  <div class="sign-line abs" style="left:521px;width:182px"></div>
  <span class="sign-label abs" style="left:27px">Handtekening</span>
  <span class="sign-label abs" style="left:522px">Datum</span>

  <footer class="footer abs">
    <span style="left:27px">Offerte #MR-000280 v1</span>
    <span style="right:27px">Pagina 6 Van 7</span>
  </footer>
</div>
</body>
</html>
```